Website for Apartment Rental in Prague

I would like to create designs of my website focused on luxury apartment rentals in Prague, Czech Republic. I created initial mock-ups, They are all attached. I need to design homepage and subpage. The mock-ups were created by combining elements from different websites that I liked but I need you to create a design that is unique and original. The attached files a only a guidance for the structure of the website but not for the design. Try to be creative.

Industry/Entity Type

Apartment

```html
<!DOCTYPE html>
<html lang="en">
<head>
<meta charset="utf-8">
<title>Maison Vltava – Being Home In Prague</title>
<link href="https://fonts.googleapis.com/css2?family=Gilda+Display&family=Work+Sans:wght@400;500;600&display=swap" rel="stylesheet">
<style>
:root{
  --gold:#d8900b;
  --gold-soft:#e9b768;
  --navy:#1d2233;
  --ink:#2b2b2b;
  --muted:#6b6b6b;
  --line:#e4e4e4;
  --panel:#f5f5f7;
  --white:#fff;
  --serif:"Gilda Display", Georgia, serif;
  --sans:"Work Sans", Arial, sans-serif;
}
*{box-sizing:border-box;margin:0;padding:0}
html,body{width:1200px;height:3974px;overflow:hidden}
body{position:relative;background:var(--white);font-family:var(--sans);color:var(--ink);font-size:13px}
.abs{position:absolute}
.gold{color:var(--gold)}
.photo{position:absolute}

/* header */
.topbar{left:0;top:0;width:1200px;height:68px;font-size:12px;color:#333}
.topbar .left{position:absolute;left:111px;top:25px;display:flex;align-items:center;gap:18px}
.lang{border:1px solid #999;padding:2px 6px;font-size:11px}
.brand{position:absolute;left:516px;top:12px;width:168px;height:44px;border:2px solid var(--navy);display:flex;align-items:center;justify-content:center;font-weight:600;font-size:15px;color:var(--navy)}
.topbar .right{position:absolute;right:111px;top:25px;display:flex;gap:28px;align-items:center}
.ico{display:inline-flex;align-items:center;gap:8px}
.navbar{left:0;top:68px;width:1200px;height:38px;background:var(--navy);display:flex;justify-content:center;gap:30px;align-items:center}
.navbar a{color:#fff;text-decoration:none;font-size:12.5px;font-weight:500}

/* hero */
.hero{left:0;top:106px;width:1200px;height:477px;
  background:
    radial-gradient(ellipse 150px 120px at 600px 300px,rgba(150,190,110,.85),rgba(150,190,110,0) 100%),
    radial-gradient(ellipse 330px 210px at 600px 270px,rgba(255,255,252,.95),rgba(255,255,252,0) 100%),
    radial-gradient(ellipse 160px 120px at 95px 270px,rgba(120,140,110,.55),rgba(120,140,110,0) 100%),
    radial-gradient(ellipse 90px 160px at 1080px 320px,rgba(150,80,40,.75),rgba(150,80,40,0) 100%),
    radial-gradient(ellipse 260px 70px at 380px 455px,rgba(40,40,45,.85),rgba(40,40,45,0) 100%),
    radial-gradient(ellipse 260px 70px at 830px 455px,rgba(40,40,45,.85),rgba(40,40,45,0) 100%),
    linear-gradient(180deg,#e6e3df 0%,#ddd8d2 45%,#b7a794 78%,#6b5440 100%)}
.hero h1{position:absolute;top:62px;width:100%;text-align:center;font-family:var(--serif);font-weight:400;font-size:50px;color:#222}
.hero .sub{position:absolute;top:127px;width:100%;text-align:center;font-size:13px;line-height:19px;color:#333}
.hero .promise{position:absolute;top:410px;width:100%;text-align:center;color:#fff;font-size:19px;text-shadow:0 1px 4px rgba(0,0,0,.5)}
.booking{left:111px;top:551px;width:975px;height:53px;background:#fff;border:2px solid var(--gold);display:flex;align-items:center;font-size:11.5px}
.booking .f{padding:0 18px;height:100%;display:flex;align-items:center;gap:10px;border-right:1px solid var(--line);white-space:nowrap}
.booking .cta{background:var(--gold);color:#fff;font-weight:600;height:100%;display:flex;align-items:center;padding:0 16px;white-space:nowrap}

/* about */
.about-photo{left:0;top:694px;width:530px;height:321px;
  background:
    radial-gradient(ellipse 110px 130px at 80px 90px,rgba(255,255,250,.95),rgba(255,255,250,0) 100%),
    radial-gradient(ellipse 120px 60px at 380px 240px,rgba(105,135,85,.9),rgba(105,135,85,0) 100%),
    radial-gradient(ellipse 90px 70px at 140px 230px,rgba(220,170,170,.7),rgba(220,170,170,0) 100%),
    radial-gradient(ellipse 240px 60px at 300px 300px,rgba(160,100,55,.8),rgba(160,100,55,0) 100%),
    linear-gradient(135deg,#f2eee7 0%,#e5ddd0 50%,#c9b293 100%)}
.h2{font-family:var(--serif);font-weight:400;font-size:34px;line-height:40px;color:#222}
.about-text{left:615px;top:716px;width:480px}
.about-text .dots{width:58px;border-top:2px dotted var(--gold);margin:10px 0 16px}
.body{font-size:13px;line-height:20px;color:#555}
.pager{display:flex;gap:14px}
.pager span{width:32px;height:32px;border-radius:50%;border:2px solid #333;display:flex;align-items:center;justify-content:center;font-size:11px;font-weight:600}
.pager span.on{border-color:var(--gold);color:var(--gold)}

/* interiors */
.interiors{left:0;top:1094px;width:1200px;height:541px;
  background:
    radial-gradient(ellipse 260px 200px at 120px 80px,rgba(255,255,255,.95),rgba(255,255,255,0) 100%),
    radial-gradient(ellipse 60px 220px at 400px 300px,rgba(235,205,190,.7),rgba(235,205,190,0) 100%),
    radial-gradient(ellipse 130px 330px at 1100px 250px,rgba(190,140,100,.85),rgba(190,140,100,0) 100%),
    radial-gradient(ellipse 260px 110px at 1000px 460px,rgba(255,255,255,.95),rgba(255,255,255,0) 100%),
    radial-gradient(ellipse 40px 45px at 835px 400px,rgba(250,248,245,1),rgba(250,248,245,0) 100%),
    linear-gradient(90deg,#fbf8f4 0%,#f4eee8 40%,#ebe8e4 70%,#ded6cd 100%)}
.interiors .txt{position:absolute;left:111px;top:68px;width:520px}
.btn-line{display:inline-flex;align-items:center;gap:12px;border:2px solid var(--gold);color:var(--gold);font-weight:600;font-size:12.5px;padding:14px 18px;background:rgba(255,255,255,.6)}

/* homes */
.center{width:1200px;text-align:center;left:0}
.card{width:308px;height:408px;background:#fff;box-shadow:0 4px 18px rgba(0,0,0,.08)}
.card .img{height:167px}
.card .in{padding:20px 24px}
.card h3{font-family:var(--serif);font-weight:400;font-size:15px;line-height:20px;color:#222}
.card p{font-size:11.5px;line-height:16px;color:#666;margin-top:10px;height:48px;overflow:hidden}
.feat{display:flex;border-top:1px solid var(--line);border-bottom:1px solid var(--line);margin:10px 0 18px;padding:8px 0}
.feat div{flex:1;text-align:center;font-size:10px;color:#777;border-right:1px solid var(--line)}
.feat div:last-child{border:0}
.btns{display:flex;gap:12px}
.b-gold{background:var(--gold);color:#fff;font-weight:600;font-size:12px;padding:10px 22px}
.b-out{border:2px solid #222;font-weight:600;font-size:12px;padding:8px 20px}

/* superior */
.sup-panel{left:543px;top:2393px;width:543px;height:390px;background:var(--panel)}
.sup-photo{left:119px;top:2332px;width:459px;height:371px;
  background:
    radial-gradient(ellipse 90px 40px at 170px 150px,rgba(255,240,200,.9),rgba(255,240,200,0) 100%),
    radial-gradient(ellipse 120px 80px at 90px 260px,rgba(110,120,135,.75),rgba(110,120,135,0) 100%),
    radial-gradient(ellipse 90px 110px at 330px 220px,rgba(255,255,255,.8),rgba(255,255,255,0) 100%),
    radial-gradient(ellipse 260px 70px at 230px 360px,rgba(175,120,70,.85),rgba(175,120,70,0) 100%),
    linear-gradient(135deg,#f3eee6 0%,#e1d3bf 55%,#b99a77 100%)}
.amen{display:flex;gap:30px;margin:22px 0 28px}
.amen div{text-align:center;font-size:11px;color:#777}

/* news */
.news-photo1{left:193px;top:2973px;width:395px;height:252px;
  background:
    radial-gradient(ellipse 80px 100px at 70px 90px,rgba(240,240,235,.85),rgba(240,240,235,0) 100%),
    radial-gradient(ellipse 110px 60px at 240px 120px,rgba(190,180,170,.9),rgba(190,180,170,0) 100%),
    radial-gradient(ellipse 170px 50px at 200px 215px,rgba(25,20,18,.95),rgba(25,20,18,0) 100%),
    linear-gradient(135deg,#d8d2ca 0%,#8a7b6e 55%,#3a302a 100%)}
.news-box{border:1.5px solid var(--gold-soft);background:#fff}
.news-photo2{left:612px;top:3291px;width:392px;height:249px;
  background:
    radial-gradient(ellipse 40px 30px at 110px 70px,rgba(255,250,235,1),rgba(255,250,235,0) 100%),
    radial-gradient(ellipse 40px 30px at 250px 70px,rgba(255,250,235,1),rgba(255,250,235,0) 100%),
    radial-gradient(ellipse 90px 40px at 196px 200px,rgba(245,235,220,.95),rgba(245,235,220,0) 100%),
    radial-gradient(circle at 50% 45%,#c98a52 0%,#8a5228 55%,#4a2a14 100%)}
.meta{font-size:11px;display:flex;gap:24px}
.news h3{font-family:var(--serif);font-weight:400;font-size:21px;line-height:27px;color:#222;margin:12px 0 10px}
.more{color:var(--gold);font-weight:600;font-size:12px;margin-top:14px;display:flex;align-items:center;gap:10px}

/* footer */
.footer{left:0;top:3665px;width:1200px;height:309px;background:var(--navy);color:#fff}
.footer h4{font-family:var(--serif);font-weight:400;font-size:17px;margin-bottom:16px}
.footer .col{position:absolute;top:56px;font-size:11.5px;line-height:22px}
.footer .copy{position:absolute;top:272px;width:100%;text-align:center;font-size:11px}
</style>
</head>
<body>

<header class="abs topbar">
  <div class="left"><span>Our Hospitality</span><span class="lang">En ▾</span>
    <span class="ico"><svg width="10" height="16" viewBox="0 0 10 16"><rect x="1" y="1" width="8" height="14" rx="1.5" fill="none" stroke="#333" stroke-width="1.4"/></svg>Call : +420 600 123 456</span></div>
  <div class="brand">Maison Vltava</div>
  <div class="right">
    <span class="ico"><svg width="13" height="13" viewBox="0 0 13 13"><circle cx="5.5" cy="5.5" r="4" fill="none" stroke="#333" stroke-width="1.5"/><line x1="8.5" y1="8.5" x2="12" y2="12" stroke="#333" stroke-width="1.5"/></svg>Discover Prague</span>
    <span class="ico"><svg width="16" height="11" viewBox="0 0 16 11"><rect x=".7" y=".7" width="14.6" height="9.6" fill="none" stroke="#333" stroke-width="1.3"/><path d="M1 1l7 5 7-5" fill="none" stroke="#333" stroke-width="1.3"/></svg>reserve@maisonvltava.example</span>
  </div>
</header>
<nav class="abs navbar">
  <a>Apartments</a><a>Location</a><a>Services</a><a>Gallery</a><a>News</a><a>Exclusive Offers</a><a>Tours For Families</a><a>Contact Us</a>
</nav>

<section class="abs hero" role="img" aria-label="Bright living room with sofas, artwork and garden view through open doors">
  <h1>Being Home In Prague</h1>
  <p class="sub">Sed do eiusmod tempor incididunt ut labore et dolore magna aliqua.<br>Ut enim ad minim veniam,</p>
  <p class="promise">Official Site <strong>Best Price Guaranteed</strong></p>
</section>
<div class="abs booking">
  <div class="f">Pickup Date <svg width="12" height="12"><rect x="1" y="2" width="10" height="9" fill="none" stroke="#999"/></svg></div>
  <div class="f">Return Date <svg width="12" height="12"><rect x="1" y="2" width="10" height="9" fill="none" stroke="#999"/></svg></div>
  <div class="f">Adult ▾</div>
  <div class="f">Children ▾</div>
  <div class="f">Infants ▾</div>
  <div class="f" style="padding-right:40px">Promo Code</div>
  <div class="cta">Check Availability</div>
  <div class="f" style="border:0">Select Rental Unit ▾</div>
</div>

<div class="abs photo about-photo" role="img" aria-label="Sunlit apartment living room with dining table, rug and bookshelves"></div>
<div class="abs about-text">
  <h2 class="h2">A Different Vision of<br><span class="gold">Apartments</span></h2>
  <div class="dots"></div>
  <p class="body">Something spectacular has arrived in the heart of Europe.<br>Steps from Old Town, this rental experience is curated with world-class amenities, exemplary style and a level of convenience you have to experience to believe.</p>
  <p class="body gold" style="font-style:italic;margin:18px 0 22px">Experience the different vision of luxury in center of Prague.</p>
  <div class="pager"><span class="on">01</span><span>02</span><span>03</span></div>
</div>

<section class="abs interiors" role="img" aria-label="Calm white bedroom with copper lamp, vase and linen bed">
  <div class="txt">
    <svg width="58" height="58" viewBox="0 0 58 58"><circle cx="29" cy="29" r="27" fill="#fff" stroke="var(--gold)" stroke-width="2"/><path d="M20 18h18v14H20zM20 32v10M38 32v10" fill="none" stroke="#333" stroke-width="2"/></svg>
    <h2 class="h2" style="margin-top:14px">Interiors Designed by<br><span class="gold">Maison Vltava</span></h2>
    <p class="body" style="margin:16px 0 26px;color:#444">Maison Vltava apartments offers short term and as well as long term options in our studio apartments and our one bedroom apartment homes. Our luxurious apartments and high quality customer service have allowed us to dominate the Prague apartment market with a proven track record.<br>Our years of experience and knowledge have made us a premier apartment rental company as we continue to stress the importance of servicing individuals and corporations who are seeking the finest accommodations.</p>
    <span class="btn-line">Find Your Home <svg width="22" height="8"><path d="M0 4h20M16 1l4 3-4 3" fill="none" stroke="var(--gold)" stroke-width="1.5"/></svg></span>
  </div>
</section>

<h2 class="abs center h2" style="top:1710px">Home’s In Prague</h2>
<p class="abs center body" style="top:1752px">Sed do eiusmod tempor incididunt ut labore et dolore magna aliqua.<br>Ut enim ad minim veniam,</p>

<div class="abs card" style="left:111px;top:1839px">
  <div class="img" role="img" aria-label="White studio with desk, shelves and plants" style="background:radial-gradient(ellipse 60px 70px at 80px 80px,rgba(110,140,90,.7),rgba(110,140,90,0) 100%),radial-gradient(ellipse 80px 60px at 230px 70px,rgba(255,255,255,.95),rgba(255,255,255,0) 100%),linear-gradient(180deg,#f4f1ec 0%,#e6ddd0 60%,#c39b6c 100%)"></div>
  <div class="in"><h3>BRAND NEW Luxury Living Shinning Contemporary Design</h3><p>The 22nd house is dedicated to colors...</p>
  <div class="feat"><div>Max 4 people</div><div>CarGarage</div><div>1 Bedroom</div></div>
  <div class="btns"><span class="b-gold">See Detail</span><span class="b-out">Book Now</span></div></div>
</div>
<div class="abs card" style="left:448px;top:1839px">
  <div class="img" role="img" aria-label="Grey modern living room with sofa and television" style="background:radial-gradient(ellipse 90px 50px at 150px 130px,rgba(70,70,75,.7),rgba(70,70,75,0) 100%),radial-gradient(ellipse 60px 80px at 40px 60px,rgba(255,255,255,.9),rgba(255,255,255,0) 100%),linear-gradient(180deg,#ebe9e6 0%,#c9c5c0 60%,#8f8780 100%)"></div>
  <div class="in"><h3>BRAND NEW ZEN Luxury Living Apartment in the Center of Prague</h3><p>Recognized with Wanderlust Journal 2017 Readers' Choice Award #1 hotel in the world,...</p>
  <div class="feat"><div>Max 4 people</div><div>CarGarage</div><div>1 Bedroom</div></div>
  <div class="btns"><span class="b-gold">See Detail</span><span class="b-out">Book Now</span></div></div>
</div>
<div class="abs card" style="left:782px;top:1839px">
  <div class="img" role="img" aria-label="Apartment with green dining table and bookshelves" style="background:radial-gradient(ellipse 80px 40px at 200px 130px,rgba(105,135,85,.9),rgba(105,135,85,0) 100%),radial-gradient(ellipse 60px 80px at 50px 60px,rgba(255,255,250,.95),rgba(255,255,250,0) 100%),linear-gradient(180deg,#f1ece4 0%,#ddd2c2 60%,#b48b5e 100%)"></div>
  <div class="in"><h3>EXPEDITION PRAGUE! TOP Locs Brand New Apartment</h3><p>For your Management committes, showroom session. Incentive trip, product launch. privatisation...</p>
  <div class="feat"><div>Max 4 people</div><div>CarGarage</div><div>1 Bedroom</div></div>
  <div class="btns"><span class="b-gold">See Detail</span><span class="b-out">Book Now</span></div></div>
</div>

<div class="abs sup-panel">
  <div style="position:absolute;left:127px;top:62px;width:370px">
    <h2 class="h2" style="font-size:30px">Superior Apartment</h2>
    <p class="body" style="margin-top:8px">Our 2 floor Superior Apartment is our smaller apartment, offering guests a mix of luxury, comfort and space in 2 bedrooms, 2 bathrooms &amp; a living area..</p>
    <div class="amen">
      <div><svg width="26" height="22"><rect x="3" y="6" width="20" height="14" fill="none" stroke="#999" stroke-width="1.5"/></svg><br>2,361 ft2</div>
      <div><svg width="26" height="22"><path d="M3 20V9l10-6 10 6v11" fill="none" stroke="#999" stroke-width="1.5"/></svg><br>Garage</div>
      <div><svg width="26" height="22"><path d="M2 18V6M2 13h22v5M6 13V9h8v4" fill="none" stroke="#999" stroke-width="1.5"/></svg><br>4 Bedroom</div>
      <div><svg width="26" height="22"><path d="M3 11h20v4a5 5 0 0 1-5 5H8a5 5 0 0 1-5-5z" fill="none" stroke="#999" stroke-width="1.5"/></svg><br>3 Baths</div>
    </div>
    <span class="btn-line" style="padding:11px 20px">See The Details <svg width="16" height="8"><path d="M0 4h14M10 1l4 3-4 3" fill="none" stroke="var(--gold)" stroke-width="1.5"/></svg></span>
  </div>
</div>
<div class="abs photo sup-photo" role="img" aria-label="Open-plan apartment with sofa, pendant lamp and bedroom"></div>
<div class="abs pager" style="left:539px;top:2729px"><span class="on">01</span><span>02</span><span>03</span></div>

<h2 class="abs center h2" style="top:2856px">Latest News</h2>
<p class="abs center body" style="top:2898px">Lorem ipsum dolor sit amet, consectetur adipisicing elit, sed do eiusmod tempor<br>incididunt ut labore et dolore magna aliqua.</p>

<div class="abs news-box news" style="left:196px;top:3008px;width:890px;height:257px">
  <div style="position:absolute;left:498px;top:28px;width:350px">
    <div class="meta"><span class="gold">Lukas Marek</span><span>July 7, 2017</span></div>
    <h3>Street Map Live adds virtual<br>reality support</h3>
    <p class="body" style="font-size:12.5px;line-height:19px">Traction seed money infographic accelerator pivot value proposition ownership business-to-consumer iteration market analytics paradigm</p>
    <div class="more">See The Details <svg width="14" height="8"><path d="M0 4h12M8 1l4 3-4 3" fill="none" stroke="var(--gold)" stroke-width="1.5"/></svg></div>
  </div>
</div>
<div class="abs photo news-photo1" role="img" aria-label="Living room with dark coffee table and cream sofa"></div>
<div class="abs" style="left:588px;top:3066px;width:88px;border-top:1.5px solid #555"></div>

<div class="abs news-box news" style="left:111px;top:3326px;width:893px;height:254px">
  <div style="position:absolute;left:82px;top:28px;width:360px">
    <div class="meta"><span class="gold">Lukas Marek</span><span>July 7, 2017</span></div>
    <h3>Street Map Live adds virtual<br>reality support</h3>
    <p class="body" style="font-size:12.5px;line-height:19px">Traction seed money infographic accelerator pivot value proposition ownership business-to-consumer iteration market analytics paradigm</p>
    <div class="more">See The Details <svg width="14" height="8"><path d="M0 4h12M8 1l4 3-4 3" fill="none" stroke="var(--gold)" stroke-width="1.5"/></svg></div>
  </div>
</div>
<div class="abs photo news-photo2" role="img" aria-label="Attic bedroom with wooden beams and skylights"></div>
<div class="abs" style="left:530px;top:3381px;width:82px;border-top:1.5px solid #555"></div>

<footer class="abs footer">
  <div class="col" style="left:111px;width:260px">
    <h4>About Us</h4>
    <p>Lorem ipsum dolor sit amet, consectetur adipiscing elit, sed do eiusmod tempor incididunt ut labore et dolore magna aliqua. Ut enim ad minim veniam, quis nostrud exercitation ullamco...</p>
  </div>
  <div class="col" style="left:446px">
    <h4>QuickLinks</h4>
    <p>Help<br>About Us<br>Terms and Conditions<br>Privacy Policy<br>Site Map</p>
  </div>
  <div class="col" style="left:614px;top:95px"><p>Help<br>About Us<br>Terms and Conditions<br>Privacy Policy<br>Site Map</p></div>
  <div class="col" style="left:780px;width:310px">
    <h4>Contact Us</h4>
    <div style="display:grid;grid-template-columns:78px 1fr">
      <span>Address:</span><span>Maison Vltava Rentals<br>12 Riverside Lane #204<br>Lakeview, NY 10001</span>
      <span>Phone:</span><span>1-800-555-0142</span>
      <span>Email:</span><span>info@maisonvltava.example</span>
    </div>
  </div>
  <p class="copy">Copyright © 2017 Maison Vltava Rentals in Prague. All rights reserved.</p>
</footer>

</body>
</html>
```